A new presentation to our clients

we are a Real Estate agency, our website is www.dorelumia.com and it’s time to have a new, fashion and remarcable Business Card. we want to differentiate ourselves from other companies so we want a business card that differentiates us. we want the business card to impact our customers. in the competitive market that we have today, we have to be different and it is this difference that we seek

Target Market(s)

Real Estate Clients

Contact Information for Business Card

We search a totaly diferent card from the usual

Font styles to use
Sans Serif

Colors
e34197

Requirements
Must have
• Logo, adress, phone contact, e-mail, photo, and our website
Nice to have
• We would like to see a modern business card
Should not have
• Houses or building draws

```html
<!DOCTYPE html>
<html lang="en">
<head>
<meta charset="utf-8">
<title>Dore Lumia – Business Card</title>
<link href="https://fonts.googleapis.com/css2?family=Montserrat:wght@400;500;600;700&display=swap" rel="stylesheet">
<style>
  :root {
    --brand-pink: #e34197;
    --brand-pink-deep: #c9307f;
    --paper: #f6f6f4;
    --ink: #3a3a3a;
    --stage: #d9d9d9;
  }
  * { box-sizing: border-box; margin: 0; padding: 0; }
  html, body { width: 1200px; height: 1200px; overflow: hidden; }
  body {
    background: var(--stage);
    font-family: "Montserrat", sans-serif;
    position: relative;
  }
  .card {
    position: absolute;
    left: 220px;
    width: 760px;
    height: 434px;
    border-radius: 4px;
    box-shadow: 0 10px 30px rgba(0,0,0,0.18);
    overflow: hidden;
  }
  .card-front {
    top: 140px;
    background: linear-gradient(120deg, var(--brand-pink-deep), var(--brand-pink));
    display: flex;
    flex-direction: column;
    align-items: center;
    justify-content: center;
  }
  .front-wordmark {
    color: var(--paper);
    font-weight: 600;
    font-size: 76px;
    letter-spacing: 1px;
  }
  .front-url {
    position: absolute;
    bottom: 44px;
    left: 0; right: 0;
    text-align: center;
    color: var(--paper);
    font-size: 16px;
    font-weight: 500;
    letter-spacing: 0.5px;
  }
  .card-back {
    top: 626px;
    background: var(--paper);
  }
  .back-wordmark {
    position: absolute;
    left: 46px;
    top: 120px;
    color: var(--brand-pink);
    font-weight: 600;
    font-size: 50px;
  }
  .details {
    position: absolute;
    left: 420px;
    top: 100px;
    width: 300px;
    color: var(--ink);
  }
  .person-name {
    color: var(--brand-pink);
    font-weight: 700;
    font-size: 24px;
    line-height: 1.1;
  }
  .person-role {
    font-weight: 600;
    font-size: 17px;
    margin-top: 2px;
  }
  .rule {
    height: 2px;
    background: var(--brand-pink);
    margin: 12px 0 10px;
  }
  .address { font-size: 15px; line-height: 1.35; }
  .contact-list { list-style: none; }
  .contact-list li {
    display: flex;
    align-items: center;
    gap: 8px;
    font-size: 16px;
    line-height: 1.45;
  }
  .contact-list svg { width: 14px; height: 14px; fill: var(--brand-pink); flex: none; }
  .bottom-band {
    position: absolute;
    left: 0; right: 0;
    bottom: 22px;
    height: 12px;
    background: var(--brand-pink);
  }
</style>
</head>
<body>
  <section class="card card-front">
    <div class="front-wordmark">Dore Lumia</div>
    <div class="front-url">www.dorelumia.com</div>
  </section>

  <section class="card card-back">
    <div class="back-wordmark">Dore Lumia</div>
    <div class="details">
      <div class="person-name">Mara Velinescu</div>
      <div class="person-role">Managing Director</div>
      <div class="rule"></div>
      <p class="address">Rua das Flores Altas, 148<br>4410-205, Porto Sul</p>
      <div class="rule"></div>
      <ul class="contact-list">
        <li>
          <svg viewBox="0 0 24 24" aria-hidden="true"><path d="M6.6 10.8a15.1 15.1 0 0 0 6.6 6.6l2.2-2.2a1 1 0 0 1 1-.25 11.4 11.4 0 0 0 3.6.57 1 1 0 0 1 1 1V20a1 1 0 0 1-1 1A17 17 0 0 1 3 4a1 1 0 0 1 1-1h3.5a1 1 0 0 1 1 1c0 1.25.2 2.45.57 3.6a1 1 0 0 1-.25 1z"/></svg>
          (+351) 210 555 140
        </li>
        <li>
          <svg viewBox="0 0 24 24" aria-hidden="true"><path d="M6 2h12v5H6zM4 8h16a2 2 0 0 1 2 2v7h-4v5H6v-5H2v-7a2 2 0 0 1 2-2zm4 8v4h8v-4z"/></svg>
          (+351) 210 555 149
        </li>
        <li>
          <svg viewBox="0 0 24 24" aria-hidden="true"><path d="M2 5h20v14H2zm2 2v.5l8 5 8-5V7z"/></svg>
          geral@dorelumia.com
        </li>
        <li>
          <svg viewBox="0 0 24 24" aria-hidden="true"><circle cx="12" cy="12" r="10"/></svg>
          www.dorelumia.com
        </li>
      </ul>
    </div>
    <div class="bottom-band"></div>
  </section>
</body>
</html>
```